Real Estate Business card design

Company Name: Tamarind Holdings, LLC
subtitle: We pay cash for houses!
Daniel Whitcombe
Managing Director
555-214-0963
Dan@TamarindHoldingsLLC.example
www.TamarindHoldingsLLC.example

We pay referral fees for Seller and Buyer leads.

Back:
We offer referral fees for Seller and Buyer leads that close.

Please contact Hal at 555-214-0963 with your referrals or to learn more about the referral program!

I am open to different color options but I am going for a classic, elegant, clean, and professional look. Please use logo as a reference.

Target Market(s)

People selling their homes and people in the market for buying homes.

Contact Information for Business Card

please see project description

Font styles to use
Serif
Sans Serif
Script

Requirements
Must have
• must have my logo in it
Nice to have
• I like cards that are split down the middle but please come up with a few mock ups. Open to any color scheme.

```html
<!DOCTYPE html>
<html lang="en">
<head>
<meta charset="utf-8">
<title>Tamarind Holdings, LLC – Business Card</title>
<link rel="stylesheet" href="https://fonts.googleapis.com/css2?family=Lato:wght@400;700&display=swap">
<style>
  :root {
    --backdrop: #e4e7ec;
    --card-white: #fbfbfa;
    --card-navy: #2a313d;
    --gold: #c9a063;
    --ink: #3a3f47;
    --ink-soft: #5b616b;
    --logo-grey: #5f6670;
    --paper-white: #f4f4f2;
  }
  * { box-sizing: border-box; margin: 0; padding: 0; }
  html, body {
    width: 1200px;
    height: 900px;
    overflow: hidden;
    background: var(--backdrop);
    font-family: "Lato", "Helvetica Neue", Arial, sans-serif;
  }
  .sheet {
    width: 1200px;
    height: 900px;
    display: flex;
    align-items: center;
    justify-content: center;
    gap: 40px;
  }
  .card {
    position: relative;
    width: 540px;
    height: 309px;
    border-radius: 3px;
    box-shadow: 0 2px 6px rgba(30, 36, 46, 0.12);
  }

  /* Front */
  .card--front { background: var(--card-white); color: var(--ink); }
  .brand {
    position: absolute;
    display: flex;
    flex-direction: column;
    align-items: flex-end;
  }
  .card--front .brand { top: 48px; right: 40px; }
  .brand__row { display: flex; align-items: center; gap: 10px; }
  .brand__mark {
    width: 14px;
    height: 14px;
    background: var(--gold);
  }
  .brand__name {
    font-size: 22px;
    font-weight: 700;
    color: var(--logo-grey);
    letter-spacing: 0.2px;
  }
  .brand__tagline {
    margin-top: 4px;
    font-size: 12px;
    color: var(--ink-soft);
  }
  .contact {
    position: absolute;
    left: 40px;
    bottom: 40px;
  }
  .contact__name {
    font-size: 19px;
    font-weight: 700;
    color: var(--gold);
  }
  .contact__phone {
    font-size: 17px;
    color: var(--ink);
    margin-top: 2px;
  }
  .contact__links {
    margin-top: 22px;
    font-size: 12px;
    line-height: 1.55;
    color: var(--ink-soft);
  }
  .contact__note {
    margin-top: 16px;
    font-size: 12px;
    line-height: 1.55;
    color: var(--ink-soft);
    max-width: 200px;
  }

  /* Back */
  .card--back { background: var(--card-navy); color: var(--paper-white); }
  .card--back .brand { top: 58px; right: 80px; }
  .card--back .brand__name { color: var(--paper-white); font-size: 26px; }
  .card--back .brand__mark { width: 16px; height: 16px; }
  .referral {
    position: absolute;
    left: 30px;
    right: 30px;
    bottom: 56px;
    text-align: center;
    font-size: 13px;
    line-height: 1.7;
  }
  .referral p + p { margin-top: 4px; }
  .referral .highlight { color: var(--gold); }
</style>
</head>
<body>
  <main class="sheet">
    <section class="card card--front" aria-label="Business card front">
      <div class="brand">
        <div class="brand__row">
          <span class="brand__mark"></span>
          <span class="brand__name">Tamarind Holdings, LLC</span>
        </div>
        <span class="brand__tagline">We pay cash for houses!</span>
      </div>
      <div class="contact">
        <h1 class="contact__name">Daniel Whitcombe</h1>
        <p class="contact__phone">555-214-0963</p>
        <p class="contact__links">
          Dan@TamarindHoldingsLLC.example<br>
          www.TamarindHoldingsLLC.example
        </p>
        <p class="contact__note">We pay referral fees for Seller and Buyer leads.</p>
      </div>
    </section>

    <section class="card card--back" aria-label="Business card back">
      <div class="brand">
        <div class="brand__row">
          <span class="brand__mark"></span>
          <span class="brand__name">Tamarind Holdings, LLC</span>
        </div>
      </div>
      <div class="referral">
        <p>We offer referral fees for Seller and Buyer leads that close.</p>
        <p>Please contact <span class="highlight">Hal</span> at <span class="highlight">555-214-0963</span> with your referrals<br>or to learn more about the referral program!</p>
      </div>
    </section>
  </main>
</body>
</html>
```